Create a Graphic About YOURSELF and PixelHarbor

PixelHarbor would like you (designers) to create an awesome graphic to promote YOURSELF and your profile on PixelHarbor!

Your graphic should communicate your name, your services and should mention PixelHarbor.

The design should be perfect for sharing on Chatterly. Here's an example of what we'd like http://blog.pixelharbor-example.ca/article/333/pixelharbor-launches-3000-hire-me-social-design-contest

Once you submitted your design, we'd love you to share the design ('advertisement') and promote yourself and PixelHarbor to your friends and potential customers. So make your submissions great and get your friends to vote for your design by 'Liking' it on Chatterly!

Prizes:
$1500 - "PixelHarbor Community" prize awarded to the designer with the most Chatterly 'Likes'
5 x $50 for the next 5 'most liked' designs on Chatterly

$1000 - "Hire Me" prize awarded to the designer who receives the most client invites
5 x $50 for the next 5 'most invited' designers

In summary, this is a great opportunity for you to increase your exposure to PixelHarbor customers and win cash prizes. Show off your design skills and get hired by PixelHarbor customers from around the world!

Target Market(s)

Fans, friends and customers of YOU

Industry/Entity Type

Cash

Requirements
Must have
• 1) Include your PixelHarbor user name on the graphic so customers can find you in the PixelHarbor Designer Directory
2) Include the tagline "Hire Me on PixelHarbor.com!" in your graphic design.
3) Share your design's URL on our Chatterly wall at http://chatterly-example.com/pixelharbor and get your friends to 'like' your design.
Nice to have
• 1) Include a tagline that expresses your design approach/philosophy
2) Artwork dimensions: 403 x 403 px
3) You can submit more than 1 design!
Should not have
• You must own the copyright of any images you use including stock imagery.

```html
<!DOCTYPE html>
<html lang="en">
<head>
<meta charset="utf-8">
<title>VectorNomad – Footprints of Design</title>
<link rel="stylesheet" href="https://fonts.googleapis.com/css2?family=Josefin+Sans:wght@300;400;600&family=Arimo:wght@700&display=swap">
<style>
  :root {
    --ink: #000000;
    --sand: #f5d08a;
    --gold-text: #f2cc86;
    --silver: #bdbdbd;
    --white: #f4f4f4;
    --steel: #5f93ad;
    --band-text: #2e2e2e;
    --link-blue: #1b5fb0;
    --placeholder: #8a6a3a;
  }
  html, body { margin: 0; padding: 0; overflow: hidden; background: var(--ink); }
  .poster {
    position: relative; width: 1200px; height: 1137px; overflow: hidden;
    background: var(--ink); font-family: "Josefin Sans", sans-serif;
  }
  .abs { position: absolute; margin: 0; white-space: nowrap; }

  .brand-mark { left: 32px; top: 92px; display: flex; align-items: center; gap: 10px; }
  .brand-mark .dot { width: 40px; height: 40px; border-radius: 50%; background: var(--silver); }
  .brand-mark .name { font-size: 22px; font-weight: 600; color: var(--white); letter-spacing: 1px; }

  .studio-city { color: var(--silver); font-size: 16px; font-weight: 600; letter-spacing: 3px; line-height: 20px; }
  .city-1 { left: 282px; top: 86px; }
  .city-2 { left: 268px; top: 135px; }

  .regions { left: 911px; top: 48px; width: 140px; text-align: center; color: var(--steel);
    font-size: 16px; font-weight: 600; letter-spacing: 3px; line-height: 32px; }
  .partner-dot { left: 1049px; top: 45px; width: 100px; height: 100px; border-radius: 50%; background: var(--steel); }

  .headline { left: 0; width: 1288px; top: 238px; text-align: center; color: var(--white);
    font-size: 26px; letter-spacing: 17px; font-weight: 400; line-height: 30px; }
  .subhead { left: 0; width: 1288px; top: 298px; text-align: center; color: var(--white);
    font-size: 16px; letter-spacing: 8px; line-height: 20px; }

  .studio-label { left: 34px; top: 380px; color: var(--gold-text); font-size: 16px; letter-spacing: 3px;
    line-height: 34px; font-weight: 400; }
  .services { right: 57px; top: 380px; text-align: right; color: var(--gold-text);
    font-size: 16px; letter-spacing: 2.6px; line-height: 34px; }

  .footprint { left: 246px; top: 366px; width: 651px; height: 478px; background: var(--placeholder); }
  .footprint-name { left: 38px; top: 742px; color: var(--white); font-size: 56px; font-weight: 300;
    letter-spacing: 3px; line-height: 56px; transform-origin: 0 100%; transform: rotate(-21deg); }

  .association-band { left: 0; top: 953px; width: 1200px; height: 146px; background: var(--sand);
    color: var(--band-text); }
  .band-line { left: 0; width: 1200px; text-align: center; font-size: 16px; line-height: 20px; }
  .band-intro { top: 14px; letter-spacing: 4px; }
  .partner-line { left: 0; width: 1200px; top: 44px; display: flex; justify-content: center; align-items: center; gap: 10px; }
  .partner-line .square { width: 28px; height: 28px; background: var(--steel); }
  .partner-line .partner-name { font-size: 28px; font-weight: 600; line-height: 30px; color: var(--band-text); }
  .partner-line .partner-site { font-family: "Arimo", sans-serif; font-weight: 700; font-size: 17px; color: #555; }
  .band-hire { top: 83px; letter-spacing: 2.4px; }
  .portfolio-url { top: 112px; font-family: "Arimo", sans-serif; font-weight: 700; font-size: 17px;
    color: var(--link-blue); letter-spacing: 1.5px; }

  .footer-bar { left: 0; top: 1099px; width: 1200px; height: 38px; line-height: 38px; text-align: center;
    font-family: "Arimo", sans-serif; font-weight: 700; font-size: 18px; color: var(--sand); letter-spacing: 2.6px; }
</style>
</head>
<body>
<main class="poster">
  <div class="abs brand-mark"><span class="dot"></span><span class="name">VectorNomad</span></div>
  <p class="abs studio-city city-1">SYDNEY</p>
  <p class="abs studio-city city-2">AUSTRALIA</p>

  <p class="abs regions">USA<br>CANADA<br>AUSTRALIA</p>
  <div class="abs partner-dot"></div>

  <h1 class="abs headline">FOOTPRINTS</h1>
  <p class="abs subhead">OF DESIGN</p>

  <p class="abs studio-label">STUDIO<br>OF<br>GRAPHIC<br>DESIGN</p>

  <div class="abs footprint" role="img" aria-label="Photograph of a bare footprint pressed into golden beach sand"></div>
  <p class="abs footprint-name">VectorNomad</p>

  <p class="abs services">VECTORNOMAD OFFERS<br>EXTENSIVE<br>INDUSTRY<br>EXPERIENCE TO<br>ASSIST YOU WITH<br>YOUR DESIGN<br>REQUIREMENTS &amp;<br>CONCEPTS IN<br>CORPORATE<br>BRANDING, WEB<br>PRESENCE, PRINT<br>MEDIA,<br>PROMOTIONS &amp;<br>STATIONERY SUITES</p>

  <section class="abs association-band">
    <p class="abs band-line band-intro">WORKING IN ASSOCIATION WITH</p>
    <div class="abs partner-line">
      <span class="square"></span>
      <span class="partner-name">PixelHarbor</span>
      <span class="partner-site">www.pixelharbor-example.com</span>
    </div>
    <p class="abs band-line band-hire">HIRE VECTORNOMAD ON PIXELHARBOR &amp; VIEW DESIGN PORTFOLIO AT</p>
    <p class="abs band-line portfolio-url">http://designers.pixelharbor-example.com/designer/23842/vectornomad</p>
  </section>

  <p class="abs footer-bar">VectorNomad Studio of Design Web Page : www.vnomad.example.com/vectornomad</p>
</main>
</body>
</html>
```